Social media design templates

A variety of templates incorporating our logo and colours to use for our postings on different social media platforms. Must be user friendly and meet our brand image. We have attached our logo to view. We would like some of the templates to offer the ability to insert a background image and others to be a template designed around our logo.

We are black and white in colour, and our values speak to our transparency and honesty, so we are looking for clean cut, sharp straight lines, not using any other colours or curved lines.

We are a recruitment company that will be using these templates
- job posting,
- general announcements,
- blog,
- company newsletter,
- updates,
- testimonials and
- top candidate profiles

We would like a gallery of templates to choose from to use separately that all represent our brand.

```html
<!DOCTYPE html>
<html lang="en">
<head>
<meta charset="utf-8">
<title>Northline Talent Group – Social Template Set</title>
<link href="https://fonts.googleapis.com/css2?family=Bebas+Neue&family=Montserrat:wght@400;500;600;700&display=swap" rel="stylesheet">
<style>
:root{
  --ink:#000;
  --panel:#141414;
  --paper:#fff;
  --grey:#555;
  --muted:#8a8a8a;
  --star:#f5a623;
  --backdrop:#1c1c1c;
}
*{box-sizing:border-box;margin:0;padding:0}
html,body{width:848px;height:1200px;overflow:hidden}
body{background:var(--backdrop);font-family:"Montserrat",sans-serif;color:var(--ink);position:relative}
.abs{position:absolute}
.photo-office{background:linear-gradient(135deg,#3a3a3a 0%,#1f1f1f 45%,#2c2c2c 70%,#151515 100%)}
.brand-box{position:absolute;background:var(--ink);display:flex;align-items:center;justify-content:center}
.brand-box::after{content:"";position:absolute;inset:8%;border:1px solid var(--paper)}
.brand-name{font-family:"Montserrat",sans-serif;font-weight:700;color:var(--paper);letter-spacing:.06em;text-align:center;line-height:1.15}
.headline{font-family:"Bebas Neue",sans-serif;line-height:.95}
.quote-mark{position:absolute;font-family:"Bebas Neue",sans-serif;color:var(--paper);line-height:1}
.stars{position:absolute;display:flex;gap:2px}
.stars svg{fill:var(--star)}
.contact-box{position:absolute;border:1.5px solid var(--ink);display:flex;align-items:center;gap:4px;padding-left:6px;font-size:5px}
.contact-box i{display:block;width:9px;height:9px;border-radius:50%;background:var(--ink);flex:none}
.btn-dark{position:absolute;background:var(--ink);color:var(--paper);display:flex;align-items:center;justify-content:center;font-weight:500}
.bullets{position:absolute;list-style:none;font-size:5.6px;line-height:2.05}
.bullets li::before{content:"▸ ";font-size:5px}

.flyer{left:23.5px;top:52px;width:390px;height:542px;background:var(--paper)}
.strip{left:23.5px;top:605px;width:392px;height:134px;background:var(--paper)}
.testimonial{left:426px;width:412px;color:var(--paper);overflow:hidden}
.testimonial .shade{position:absolute;inset:0;background:rgba(0,0,0,.55)}
.quote-body{position:absolute;line-height:1.15}
.attrib{position:absolute;font-family:"Bebas Neue",sans-serif;font-size:7.5px;letter-spacing:.01em;white-space:nowrap}
.poster{top:750px;width:405px;height:407px;background:var(--paper)}
.poster .inner{position:absolute;left:11px;top:10px;width:383px;height:385px;background:var(--panel);overflow:hidden}
.poster .scene{position:absolute;left:190px;top:0;width:193px;height:345px}
.poster .frame{position:absolute;left:7px;top:8px;width:368px;height:368px;border:1px solid var(--paper)}
.poster .headline{position:absolute;left:23px;top:28px;font-size:37px;color:var(--paper)}
.poster .rule{position:absolute;left:23px;top:145px;width:56px;height:2px;background:var(--paper)}
.poster .tag{position:absolute;left:23px;top:158px;width:95px;height:19px;background:var(--paper);font-weight:700;font-size:8px;display:flex;align-items:center;justify-content:center}
.jobs{position:absolute;left:32px;top:194px;list-style:none;color:var(--paper);font-size:8.4px;line-height:15.4px}
.jobs li::before{content:"› ";}
.jobs b{font-weight:700}
.poster-foot{position:absolute;left:0;top:345px;width:383px;height:40px;background:#0c0c0c;display:flex;align-items:center;gap:22px;padding-left:24px;color:var(--paper);font-size:6.6px}
.poster-foot span{display:flex;align-items:center;gap:5px}
.poster-foot svg{stroke:var(--paper);fill:none;stroke-width:1.2}
.poster .brand-box{left:292px;top:0;width:89px;height:75px;flex-direction:column}
.poster .brand-box::after{display:none}
</style>
</head>
<body>

<!-- Flyer -->
<section class="abs flyer">
  <div class="abs photo-office" style="left:0;top:0;width:390px;height:168px" role="img" aria-label="Greyscale photo of a team meeting in an office"></div>
  <div class="brand-box" style="left:101px;top:81px;width:188px;height:123px">
    <span class="brand-name" style="font-size:15px">NORTHLINE</span>
  </div>
  <h1 class="abs headline" style="left:0;width:390px;top:228px;text-align:center;font-size:34px;font-weight:400">NAME SURNAME</h1>
  <p class="abs" style="left:50px;top:277px;width:310px;font-size:9.4px;line-height:11.2px">Lorem ipsum dolor sit amet, consectetur adipiscing elit, sed do eiusmod tempor incididunt ut labore et dolore magna aliqua Ut enim ad minim veniam, quis nostrud exercitation ullamco nisi ut aliquip ex ea commodo consequat. Duis aute irure dolor in reprehenderit in voluptate velit esse cillum dolore eu fugiat nulla</p>
  <div class="btn-dark" style="left:50px;top:353px;width:101px;height:19px;font-size:8.6px">LOREM IPSUM</div>
  <p class="abs" style="left:50px;top:389px;width:300px;font-size:8.9px;line-height:11.2px;color:var(--grey)">Sed ut perspiciatis unde omnis iste natus error sit voluptatem accusantium doloremque laudantium, totam rem aperiam,</p>
  <ul class="bullets" style="left:60px;top:420px">
    <li>Lorem ipsum dolor sit amet, consectetur adipiscing elit,</li>
    <li>Lorem ipsum dolor sit amet, consectetur adipiscing elit,</li>
    <li>Lorem ipsum dolor sit amet, consectetur adipiscing elit,</li>
  </ul>
  <div class="contact-box" style="left:48px;top:471px;width:89px;height:24px"><i></i>info@northlinetalent.com</div>
  <div class="contact-box" style="left:142px;top:471px;width:89px;height:24px"><i></i>info@northlinetalent.com</div>
  <div class="contact-box" style="left:233px;top:471px;width:89px;height:24px"><i></i>info@northlinetalent.com</div>
</section>

<!-- Horizontal strip -->
<section class="abs strip">
  <div class="abs photo-office" style="left:0;top:0;width:118px;height:134px" role="img" aria-label="Greyscale photo of an office meeting"></div>
  <div class="brand-box" style="left:19px;top:29px;width:117px;height:77px">
    <span class="brand-name" style="font-size:9.5px">NORTHLINE</span>
  </div>
  <h2 class="abs headline" style="left:165px;top:13px;font-size:15px;font-weight:400">NAME SURNAME</h2>
  <p class="abs" style="left:165px;top:34px;width:160px;font-size:4.6px;line-height:5.6px">Lorem ipsum dolor sit amet, consectetur adipiscing elit, sed do eiusmod tempor incididunt ut labore et dolore magna aliqua Ut enim ad minim veniam, quis nostrud exercitation ullamco nisi ut aliquip ex ea commodo consequat. Duis aute irure dolor in reprehenderit in voluptate velit esse cillum dolore eu fugiat nulla</p>
  <div class="btn-dark" style="left:165px;top:73px;width:57px;height:10px;font-size:4.6px">LOREM IPSUM</div>
  <p class="abs" style="left:165px;top:87px;width:150px;font-size:4.4px;line-height:5.4px;color:var(--grey)">Sed ut perspiciatis unde omnis iste natus error sit voluptatem accusantium doloremque laudantium, totam rem aperiam,</p>
  <ul class="bullets" style="left:170px;top:101px;font-size:3px;line-height:6px">
    <li>Lorem ipsum dolor sit amet, consectetur adipiscing elit,</li>
    <li>Lorem ipsum dolor sit amet, consectetur adipiscing elit,</li>
    <li>Lorem ipsum dolor sit amet, consectetur adipiscing elit,</li>
  </ul>
  <div class="contact-box" style="left:334px;top:46px;width:49px;height:13px;font-size:2.8px;padding-left:3px;gap:2px"><i style="width:5px;height:5px"></i>info@northlinetalent.com</div>
  <div class="contact-box" style="left:334px;top:65px;width:49px;height:13px;font-size:2.8px;padding-left:3px;gap:2px"><i style="width:5px;height:5px"></i>info@northlinetalent.com</div>
  <div class="contact-box" style="left:334px;top:84px;width:49px;height:13px;font-size:2.8px;padding-left:3px;gap:2px"><i style="width:5px;height:5px"></i>info@northlinetalent.com</div>
</section>

<!-- Testimonial: large -->
<section class="abs testimonial photo-office" style="top:76px;height:293px" role="img" aria-label="Darkened photo of a team meeting around a conference table">
  <div class="shade"></div>
  <div class="abs" style="left:0;top:73px;width:412px;height:1.5px;background:var(--paper)"></div>
  <div class="brand-box" style="left:140px;top:30px;width:132px;height:86px">
    <span class="brand-name" style="font-size:11px">NORTHLINE</span>
  </div>
  <h2 class="abs headline" style="left:0;width:412px;text-align:center;top:133px;font-size:27px;font-weight:400">NAME SURNAME</h2>
  <div class="abs" style="left:0;width:412px;text-align:center;top:161px;font-size:10px;letter-spacing:.55em;font-weight:400">JOB POSITION</div>
  <span class="quote-mark" style="left:20px;top:180px;font-size:90px">“</span>
  <p class="quote-body" style="left:68px;top:190px;width:292px;font-size:8.9px">Lorem ipsum dolor sit amet, consectetur adipiscing elit, sed do eiusmod tempor incididunt ut labore et dolore magna aliqua Ut enim ad minim veniam, quis nostrud exercitation ullamco nisi ut aliquip ex ea commodo consequat. Duis aute irure dolor reprehenderit in voluptate velit esse cillum dolore eu fugiat</p>
  <span class="quote-mark" style="left:366px;top:230px;font-size:90px">”</span>
  <div class="stars" style="left:180px;top:262px">
    <svg width="11" height="11" viewBox="0 0 10 10"><polygon points="5,0 6.2,3.6 10,3.6 6.9,5.8 8.1,9.5 5,7.2 1.9,9.5 3.1,5.8 0,3.6 3.8,3.6"/></svg>
    <svg width="11" height="11" viewBox="0 0 10 10"><polygon points="5,0 6.2,3.6 10,3.6 6.9,5.8 8.1,9.5 5,7.2 1.9,9.5 3.1,5.8 0,3.6 3.8,3.6"/></svg>
    <svg width="11" height="11" viewBox="0 0 10 10"><polygon points="5,0 6.2,3.6 10,3.6 6.9,5.8 8.1,9.5 5,7.2 1.9,9.5 3.1,5.8 0,3.6 3.8,3.6"/></svg>
    <svg width="11" height="11" viewBox="0 0 10 10"><polygon points="5,0 6.2,3.6 10,3.6 6.9,5.8 8.1,9.5 5,7.2 1.9,9.5 3.1,5.8 0,3.6 3.8,3.6"/></svg>
    <svg width="11" height="11" viewBox="0 0 10 10"><polygon points="5,0 6.2,3.6 10,3.6 6.9,5.8 8.1,9.5 5,7.2 1.9,9.5 3.1,5.8 0,3.6 3.8,3.6"/></svg>
  </div>
</section>

<!-- Testimonial: logo left -->
<section class="abs testimonial photo-office" style="top:380px;height:141px" role="img" aria-label="Darkened photo of an office meeting room">
  <div class="shade"></div>
  <div class="brand-box" style="left:25px;top:30px;width:123px;height:81px">
    <span class="brand-name" style="font-size:10px">NORTHLINE</span>
  </div>
  <span class="quote-mark" style="left:160px;top:2px;font-size:64px">“</span>
  <p class="quote-body" style="left:163px;top:48px;width:240px;font-size:7px">Lorem ipsum dolor sit amet, consectetur adipiscing elit, sed do eiusmod tempor incididunt ut labore et dolore magna aliqua Ut enim ad minim veniam, quis nostrud exercitation ullamco nisi ut aliquip ex ea commodo consequat. Duis aute irure dolor reprehenderit in voluptate velit esse cillum dolore eu fugiat</p>
  <div class="stars" style="left:163px;top:100px">
    <svg width="8" height="8" viewBox="0 0 10 10"><polygon points="5,0 6.2,3.6 10,3.6 6.9,5.8 8.1,9.5 5,7.2 1.9,9.5 3.1,5.8 0,3.6 3.8,3.6"/></svg>
    <svg width="8" height="8" viewBox="0 0 10 10"><polygon points="5,0 6.2,3.6 10,3.6 6.9,5.8 8.1,9.5 5,7.2 1.9,9.5 3.1,5.8 0,3.6 3.8,3.6"/></svg>
    <svg width="8" height="8" viewBox="0 0 10 10"><polygon points="5,0 6.2,3.6 10,3.6 6.9,5.8 8.1,9.5 5,7.2 1.9,9.5 3.1,5.8 0,3.6 3.8,3.6"/></svg>
    <svg width="8" height="8" viewBox="0 0 10 10"><polygon points="5,0 6.2,3.6 10,3.6 6.9,5.8 8.1,9.5 5,7.2 1.9,9.5 3.1,5.8 0,3.6 3.8,3.6"/></svg>
    <svg width="8" height="8" viewBox="0 0 10 10"><polygon points="5,0 6.2,3.6 10,3.6 6.9,5.8 8.1,9.5 5,7.2 1.9,9.5 3.1,5.8 0,3.6 3.8,3.6"/></svg>
  </div>
  <span class="attrib" style="left:222px;top:100px">- NAME SURNAME/ NORTHLINE TALENT GROUP MEMBER</span>
  <span class="quote-mark" style="left:378px;top:86px;font-size:64px">”</span>
</section>

<!-- Testimonial: logo right -->
<section class="abs testimonial photo-office" style="top:531px;height:141px" role="img" aria-label="Darkened photo of an office meeting room">
  <div class="shade"></div>
  <span class="quote-mark" style="left:26px;top:4px;font-size:64px">“</span>
  <p class="quote-body" style="left:29px;top:50px;width:240px;font-size:7px">Lorem ipsum dolor sit amet, consectetur adipiscing elit, sed do eiusmod tempor incididunt ut labore et dolore magna aliqua Ut enim ad minim veniam, quis nostrud exercitation ullamco nisi ut aliquip ex ea commodo consequat. Duis aute irure dolor reprehenderit in voluptate velit esse cillum dolore eu fugiat</p>
  <div class="stars" style="left:29px;top:103px">
    <svg width="8" height="8" viewBox="0 0 10 10"><polygon points="5,0 6.2,3.6 10,3.6 6.9,5.8 8.1,9.5 5,7.2 1.9,9.5 3.1,5.8 0,3.6 3.8,3.6"/></svg>
    <svg width="8" height="8" viewBox="0 0 10 10"><polygon points="5,0 6.2,3.6 10,3.6 6.9,5.8 8.1,9.5 5,7.2 1.9,9.5 3.1,5.8 0,3.6 3.8,3.6"/></svg>
    <svg width="8" height="8" viewBox="0 0 10 10"><polygon points="5,0 6.2,3.6 10,3.6 6.9,5.8 8.1,9.5 5,7.2 1.9,9.5 3.1,5.8 0,3.6 3.8,3.6"/></svg>
    <svg width="8" height="8" viewBox="0 0 10 10"><polygon points="5,0 6.2,3.6 10,3.6 6.9,5.8 8.1,9.5 5,7.2 1.9,9.5 3.1,5.8 0,3.6 3.8,3.6"/></svg>
    <svg width="8" height="8" viewBox="0 0 10 10"><polygon points="5,0 6.2,3.6 10,3.6 6.9,5.8 8.1,9.5 5,7.2 1.9,9.5 3.1,5.8 0,3.6 3.8,3.6"/></svg>
  </div>
  <span class="attrib" style="left:86px;top:103px">- NAME SURNAME/ NORTHLINE TALENT GROUP MEMBER</span>
  <span class="quote-mark" style="left:242px;top:89px;font-size:64px">”</span>
  <div class="brand-box" style="left:277px;top:31px;width:123px;height:81px">
    <span class="brand-name" style="font-size:10px">NORTHLINE</span>
  </div>
</section>

<!-- Job poster: house -->
<section class="abs poster" style="left:14px">
  <div class="inner">
    <div class="scene" role="img" aria-label="Photo of a modern white house with a turquoise pool" style="background:linear-gradient(90deg,var(--panel) 0%,rgba(20,20,20,.4) 25%,transparent 45%),linear-gradient(180deg,#7a99b5 0%,#d9d9d6 40%,#b9b4aa 60%,#2fb3c7 85%,#1b8d9e 100%)"></div>
    <div class="frame"></div>
    <h2 class="headline">WE ARE<br>LOOKING FOR<br>NEW TALENTS</h2>
    <div class="rule"></div>
    <div class="tag">JOB POSITIONS</div>
    <ul class="jobs">
      <li>General Manager - Syndey - <b>$200K+</b></li>
      <li>State Manager - Syndey - <b>$150K+</b></li>
      <li>Sales Manager - Syndey - <b>$150K+</b></li>
      <li>Marketing Manager- Syndey - <b>$120K+</b></li>
      <li>Sales Consultants - Syndey - <b>Base+Comm</b></li>
      <li>Accountants Administrator- Syndey - <b>$60K</b></li>
    </ul>
    <div class="poster-foot">
      <span><svg width="8" height="8" viewBox="0 0 10 10"><rect x="1" y="2" width="8" height="6"/><polyline points="1,2 5,5.5 9,2"/></svg>info@northlinetalent.com</span>
      <span><svg width="8" height="8" viewBox="0 0 10 10"><rect x="1" y="1" width="8" height="8"/><line x1="1" y1="5" x2="9" y2="5"/><line x1="5" y1="1" x2="5" y2="9"/></svg>www.northlinetalentgroup.com</span>
      <span><svg width="8" height="8" viewBox="0 0 10 10"><path d="M2 1h2l1 2.5-1.3 1a6 6 0 0 0 2.8 2.8l1-1.3L10 7v2a1 1 0 0 1-1 1A8 8 0 0 1 1 2a1 1 0 0 1 1-1z"/></svg>000-000-0000</span>
    </div>
  </div>
  <div class="brand-box">
    <span class="brand-name" style="font-size:9px">NORTHLINE</span>
    <span class="brand-name" style="font-size:6px;font-weight:700;margin-top:3px">TALENT GROUP</span>
  </div>
</section>

<!-- Job poster: construction -->
<section class="abs poster" style="left:426px">
  <div class="inner">
    <div class="scene" role="img" aria-label="Photo of an excavator bucket pouring soil against a blue sky" style="background:linear-gradient(90deg,var(--panel) 0%,rgba(20,20,20,.4) 25%,transparent 45%),linear-gradient(180deg,#2a6fa8 0%,#6f9fc2 30%,#8a6a4a 55%,#c9832f 78%,#6a4a2a 100%)"></div>
    <div class="frame"></div>
    <h2 class="headline">WE ARE<br>LOOKING FOR<br>NEW TALENTS</h2>
    <div class="rule"></div>
    <div class="tag">JOB POSITIONS</div>
    <ul class="jobs">
      <li>General Manager - Syndey - <b>$200K+</b></li>
      <li>State Manager - Syndey - <b>$150K+</b></li>
      <li>Sales Manager - Syndey - <b>$150K+</b></li>
      <li>Marketing Manager- Syndey - <b>$120K+</b></li>
      <li>Sales Consultants - Syndey - <b>Base+Comm</b></li>
      <li>Accountants Administrator- Syndey - <b>$60K</b></li>
    </ul>
    <div class="poster-foot">
      <span><svg width="8" height="8" viewBox="0 0 10 10"><rect x="1" y="2" width="8" height="6"/><polyline points="1,2 5,5.5 9,2"/></svg>info@northlinetalent.com</span>
      <span><svg width="8" height="8" viewBox="0 0 10 10"><rect x="1" y="1" width="8" height="8"/><line x1="1" y1="5" x2="9" y2="5"/><line x1="5" y1="1" x2="5" y2="9"/></svg>www.northlinetalentgroup.com</span>
      <span><svg width="8" height="8" viewBox="0 0 10 10"><path d="M2 1h2l1 2.5-1.3 1a6 6 0 0 0 2.8 2.8l1-1.3L10 7v2a1 1 0 0 1-1 1A8 8 0 0 1 1 2a1 1 0 0 1 1-1z"/></svg>000-000-0000</span>
    </div>
  </div>
  <div class="brand-box">
    <span class="brand-name" style="font-size:9px">NORTHLINE</span>
    <span class="brand-name" style="font-size:6px;font-weight:700;margin-top:3px">TALENT GROUP</span>
  </div>
</section>

</body>
</html>
```